We are a printed circuit board manufacturer. Need a company professional web site to allow our potential customers to know more about our background, capability and our products. The web site will contain three languages, which are Chinese, English and Japanese. Our audience are mainly electronic companies that procure printed circuit boards. I have a word document that have all the required text in all three languages. The final design should communicate the impression that we embrace quality, trustworthiness and long term partnership business principles.
We should have sections that allow us to post pictures of our facilities.
I have added the three files in three different languages.
Some of the information is below:
Background
RVD Worldwide Limited (RVD) was set up in Hong Kong in 2007 by two Hong Kong entrepreneurs, Mr. Lok Fai Tam and Mr. Wai Ho. We acquired the single sided printed circuit board factory located in Dongguan City, Guangdong Province, China, from Valtor Corporation of the U.S. in 2007. In addition to RVD, Mr. Tam and Mr. Ho also own Brightrail Systems Company Limited, a semiconductor company based in Hong Kong since 1997 with a total investment of over US$100 million. Brightrail is engaged in the manufacturing of flexible substrates and MEMS assembly business.
RVD has been awarded TS 16949 and ISO14000 certificates since 2009 and 2004 respectively.
Business Principles
RVD Worldwide Limited strives to be a professional top notched printed circuit board supplier. We embrace four “EXCELLENCE” principles, namely, excellence in quality, excellence in prices, excellence in services and excellence in on time delivery.
We approach each customer with a long-term partnership view that delivers the lowest ownership costs and highest total values to our customers. We customize quotations and solutions in order to allow our customers to win more businesses. We believe by thinking from our customers’ points of view we will be able to create a WIN-WIN relationship.
Customers
Due to our excellent quality, services and production systems, RVD Worldwide Limited manage to service a number of large Japanese and US customers, which include:
Technical capability overview
Below is an overview of our current capability:
Target Market(s)
Electronic companies buyers
Industry/Entity Type
Business
Requirements
Must have
- Capability description
Should not have
- no cartoon

```html
<!DOCTYPE html>
<html lang="en">
<head>
<meta charset="utf-8">
<title>RVD Worldwide Limited</title>
<link rel="stylesheet" href="https://fonts.googleapis.com/css2?family=Ubuntu:wght@300;400;500&family=Arimo:wght@400&display=swap">
<style>
:root{
  --green:#1b7a55;
  --green-dark:#0f5c3e;
  --green-bright:#3aa33c;
  --teal:#2a9b8a;
  --ink:#333;
  --muted:#555;
  --blue:#1f86c8;
  --panel:#f1f1f1;
  --line:#d9dedb;
  --foot-top:#3a3f44;
  --foot-bot:#0c0d0e;
}
*{box-sizing:border-box;margin:0;padding:0}
html,body{width:963px;height:1200px;overflow:hidden}
body{position:relative;font-family:"Ubuntu",sans-serif;color:var(--ink);
  background:linear-gradient(180deg,#e2f0e8 0,#f3f8f5 300px,#eef6f1 600px,#fff 616px,#fff 100%)}
.abs{position:absolute}
.logo{left:98px;top:34px;display:flex;align-items:center;gap:8px;color:var(--green);font-weight:500;font-size:21px;line-height:1}
.logo .mark{width:18px;height:18px;background:var(--green)}
.logo small{display:block;font-size:11px;margin-top:3px}
.flags{left:783px;top:14px;display:flex;gap:8px}
.flags svg{width:18px;height:12px;display:block}
.nav{left:343px;top:48px;width:514px;height:31px;background:linear-gradient(#2b8f67,#14704b);border-radius:4px;display:flex;align-items:center;justify-content:space-around;padding:0 10px;box-shadow:0 2px 3px rgba(0,0,0,.15)}
.nav a{color:#fff;text-decoration:none;font-size:10.5px}
.main-panel{left:88px;top:106px;width:787px;height:472px;background:#fff;border:1px solid var(--line)}
.hero{left:98px;top:116px;width:767px;height:262px;border-radius:3px;border:1px solid #0d4038;
  background:linear-gradient(180deg,#cfe9e2 0,#5cb8a6 30%,#2a9988 60%,#137a6d 100%)}
.hero-caption{left:98px;top:185px;width:431px;height:134px;background:rgba(8,60,46,.85);color:#fff;font-size:21px;line-height:29px;padding:20px 14px}
.welcome{left:104px;top:402px;font-weight:300;font-size:25px;color:#222}
.welcome b{font-weight:400}
.intro{left:105px;top:444px;width:490px;font-family:"Arimo",sans-serif;font-size:8.4px;line-height:12px;color:var(--muted)}
.intro p+p{margin-top:11px}
.pick{left:623px;top:388px;width:238px;height:179px;background:#fff;border:1px solid #e3e3e3;box-shadow:0 4px 4px -2px rgba(0,0,0,.15)}
.pick-photo{left:643px;top:409px;width:199px;height:120px;background:linear-gradient(135deg,#2e7a3e,#6ab36a 50%,#34423a)}
.pick-tab{left:615px;top:399px;width:88px;height:19px;background:#7fa9a6;color:#fff;font-style:italic;font-size:12px;padding:2px 8px;border-radius:2px 2px 0 0}
.pick-arrow{top:444px;width:16px;height:48px;background:var(--green-bright)}
.pick-link{left:643px;top:536px;font-size:18.5px;color:var(--blue);font-weight:500}
.band{left:88px;width:787px;background:var(--panel);border:1px solid var(--line);border-radius:2px}
.band.products{top:591px;height:171px;background:#eef5f1}
.band.partners{top:775px;height:148px}
.tab{left:79px;width:115px;height:28px;background:var(--green);color:#fff;font-size:12.5px;padding:6px 0 0 23px}
.tab::after{content:"";position:absolute;left:0;bottom:-6px;border-top:6px solid #0b3f2a;border-left:8px solid transparent}
.prod-photo{left:113px;top:629px;width:162px;height:123px;background:linear-gradient(160deg,#9aa7a2,#4d6a5a 55%,#2c4638);border:1px solid #ccc}
.prod-text{left:286px;top:628px;width:340px;font-size:9.6px;line-height:14.4px;color:var(--muted);font-weight:300}
.prod-text p+p{margin-top:14px}
.chev{top:670px;font-size:30px;color:var(--green-bright);font-weight:500}
.services{left:672px;top:601px}
.services h3{font-size:14.5px;color:var(--green-dark);font-weight:500;margin-bottom:8px}
.services li{list-style:none;font-size:11px;color:var(--muted);font-weight:300;height:26px;padding-left:11px;position:relative}
.services li::before{content:"";position:absolute;left:0;top:3px;border-left:5px solid #444;border-top:3.5px solid transparent;border-bottom:3.5px solid transparent}
.brand{font-size:17px;font-weight:500;color:#1f3d8a;transform:translateX(-50%);white-space:nowrap}
footer{left:0;top:944px;width:963px;height:210px;background:linear-gradient(180deg,var(--foot-top),var(--foot-bot));color:#fff}
footer h4{position:absolute;font-weight:400;font-size:16.5px}
footer ul{position:absolute;list-style:none;font-family:"Arimo",sans-serif;font-size:9.8px;color:#ccc}
footer ul.links li{height:18.5px;padding-left:10px;position:relative}
footer ul.links li::before{content:"";position:absolute;left:0;top:5px;width:3px;height:3px;border-radius:50%;background:#ccc}
footer ul.social li{height:28px;display:flex;align-items:center;gap:10px;color:#fff}
footer ul.social i{width:24px;height:24px;background:#8ea3b4;border-radius:3px;display:block}
.contact{position:absolute;left:700px;top:44px;font-family:"Arimo",sans-serif;font-size:10px;line-height:14.5px;color:#fff;width:150px}
.copyright{left:0;top:1170px;width:963px;text-align:center;font-size:8.6px;color:#222}
</style>
</head>
<body>
<div class="abs logo"><span class="mark"></span><div>RVD Worldwide<small>Limited</small></div></div>
<div class="abs flags">
  <svg viewBox="0 0 18 12"><rect width="18" height="4" fill="#000"/><rect y="4" width="18" height="4" fill="#d00"/><rect y="8" width="18" height="4" fill="#fc0"/></svg>
  <svg viewBox="0 0 18 12"><rect width="18" height="12" fill="#ed2939"/><rect y="4" width="18" height="4" fill="#fff"/></svg>
  <svg viewBox="0 0 18 12"><rect width="18" height="12" fill="#e00"/><rect x="7.5" y="2" width="3" height="8" fill="#fff"/><rect x="5" y="4.5" width="8" height="3" fill="#fff"/></svg>
</div>
<nav class="abs nav"><a href="#">Home</a><a href="#">About Us</a><a href="#">Technology</a><a href="#">Customer Service</a><a href="#">Accessories</a><a href="#">Contact Us</a></nav>

<div class="abs main-panel"></div>
<div class="abs hero" role="img" aria-label="Photo of a man standing on a rock looking over calm teal sea"></div>
<div class="abs hero-caption">RVD is providing a RISK FREE supply of double sided and multi-layered printed circuit boards to our customers</div>

<h1 class="abs welcome">Welcome to <b>RVD International</b></h1>
<div class="abs intro">
  <p>RVD Worldwide Limited (RVD) was set up in Hong Kong in 2007 by two Hong Kong entrepreneurs, Mr. Lok Fai Tam and Mr. Wai Ho. We acquired the single sided printed circuit board factory located in Dongguan City, Guangdong Province, China, from Valtor Corporation of the U.S. in 2007. In addition to RVD, Mr. Tam and Mr. Ho also own Brightrail Systems Company Limited, a semiconductor company based in Hong Kong since 1997 with a total investment of over US$100 million. Brightrail is engaged in the manufacturing of flexible substrates and the assembly of Micro Electro Mechanical Systems (MEMS).</p>
  <p>RVD has been awarded TS 16949 and ISO14000 certificates since 2009 and 2004 respectively.</p>
</div>

<div class="abs pick"></div>
<div class="abs pick-photo" role="img" aria-label="Close-up photo of a green circuit board with components"></div>
<div class="abs pick-tab">Editors' pick</div>
<svg class="abs pick-arrow" style="left:626px" viewBox="0 0 16 48"><path d="M11 16 5 24l6 8" stroke="#fff" stroke-width="2.5" fill="none"/></svg>
<svg class="abs pick-arrow" style="left:843px" viewBox="0 0 16 48"><path d="M5 16l6 8-6 8" stroke="#fff" stroke-width="2.5" fill="none"/></svg>
<div class="abs pick-link">Technology advances &gt;&gt;</div>

<section class="abs band products"></section>
<div class="abs tab" style="top:591px">Our Products</div>
<div class="abs prod-photo" role="img" aria-label="Photo of a worker inspecting boards at a factory machine"></div>
<div class="abs prod-text">
  <p>Our own personnel are stationed at the manufacturers' production facilities 24 hours a day 7 days a week. We provide real time update on a part number by part number basis of our customers' purchase orders status online.</p>
  <p>We examine and test 100% of boards at our own facilities before we deliver to our customers. We provide warehousing services for our customers to ensure products are delivered on a just in time basis.<br>In summary, we help our customers manage their RISKS in procuring printed circuit boards.</p>
</div>
<div class="abs chev" style="left:91px">&#10094;</div>
<div class="abs chev" style="left:848px">&#10095;</div>
<div class="abs services"><h3>Services</h3><ul><li>Raw Materials</li><li>Plating</li><li>Copper Thickness</li><li>Punching and CNC Process</li><li>V cut</li></ul></div>

<section class="abs band partners"></section>
<div class="abs tab" style="top:775px">Our Products</div>
<div class="abs brand" style="left:162px;top:822px">Norvale</div>
<div class="abs brand" style="left:293px;top:822px">Kestrel</div>
<div class="abs brand" style="left:418px;top:822px">Tamura Drive</div>
<div class="abs brand" style="left:565px;top:822px">Shirako</div>
<div class="abs brand" style="left:762px;top:822px">Halden International</div>
<div class="abs brand" style="left:155px;top:877px">Mirato</div>
<div class="abs brand" style="left:300px;top:877px">Fenari</div>
<div class="abs brand" style="left:416px;top:877px">Dalmark</div>
<div class="abs brand" style="left:565px;top:877px">Hoshida</div>
<div class="abs brand" style="left:774px;top:877px">Suneko</div>

<footer class="abs">
  <h4 style="left:91px;top:17px">Quick Links</h4>
  <ul class="links" style="left:88px;top:50px"><li>Home</li><li>About Us</li><li>Custom Engering</li><li>Automation</li><li>Workshop</li><li>About</li><li>Contact</li></ul>
  <ul class="links" style="left:279px;top:49px"><li>Featured Product</li><li>Accumulation Tables</li><li>Slicer Project</li><li>Raw Materials</li><li>Punching and CNC Process</li><li>Engineering / Design Assistance</li><li>Platforms</li></ul>
  <h4 style="left:490px;top:17px">Follow Us</h4>
  <ul class="social" style="left:491px;top:49px"><li><i></i>Follow us on Friendlink</li><li><i></i>Follow us on Chirper</li><li><i></i>Follow us on ProNet</li><li><i></i>Follow us on ClipTube</li></ul>
  <h4 style="left:700px;top:16px">Contact</h4>
  <div class="contact">RVD Worldwide Limited<br>18/F Harbour Point<br>52 Marlow Road<br>Causeway Bay, HONG KONG<br><br>Telephone: (852)25550148<br>Fax: (852)25550149<br><br>Email: Sales@rvdboard.com</div>
</footer>
<div class="abs copyright">COPYRIGHT - include a copyright statement © 2012 RVD Worldwide Limited, | All rights reserved</div>
</body>
</html>
```